BRAMBLE CABS

Taxi card design

Need changes very slow in replying to my messages.

Target Market(s)

Customers

Industry/Entity Type

Taxi

Contact Information for Business Card

See previous design

Font styles to use
Sans Serif

Colors
A7469A
B969AE
D3A5CF
EDDBEB
F8F0F9
6B429C
8869AF
B7A5CE
E3DAEB
F3F0F8

Requirements
Nice to have
• We are in the business of looking after people, not just driving vehicles front
Should not have
• Front number 01832 419 526 needs to big big

```html
<!DOCTYPE html>
<html lang="en">
<head>
<meta charset="UTF-8">
<title>Bramble Cabs – Business Card</title>
<link href="https://fonts.googleapis.com/css2?family=Poppins:wght@300;400;500;600;700&display=swap" rel="stylesheet">
<style>
  :root {
    --magenta: #A7469A;
    --magenta-light: #B969AE;
    --violet: #6B429C;
    --violet-deep: #4E2C86;
    --ink: #111113;
    --card-white: #FFFFFF;
    --card-dark: #1D1D20;
    --logo-faint: #2B2B30;
    --backdrop: #3C3C3E;
    --text-grey: #222226;
    --band: linear-gradient(90deg, var(--magenta) 0%, var(--violet) 75%, var(--violet-deep) 100%);
  }
  * { box-sizing: border-box; margin: 0; padding: 0; }
  html, body {
    width: 1200px; height: 1024px; overflow: hidden;
    background: var(--backdrop);
    font-family: "Poppins", sans-serif;
  }
  .sheet {
    width: 1200px; height: 1024px;
    display: flex; flex-direction: column; align-items: center; justify-content: center;
    gap: 24px;
  }
  .card {
    position: relative;
    width: 840px; height: 480px;
    border-bottom: 3px solid var(--magenta);
    overflow: hidden;
  }

  /* ---------- front ---------- */
  .card--front { background: var(--card-white); }
  .brand {
    position: absolute; top: 44px; left: 64px;
    display: flex; align-items: center; gap: 14px;
  }
  .brand__dot {
    width: 26px; height: 26px; border-radius: 50%;
    background: var(--magenta);
  }
  .brand__name {
    font-weight: 700; font-size: 44px; line-height: 1;
    color: var(--violet); letter-spacing: 0.5px;
  }
  .front__call {
    position: absolute; top: 112px; left: 60px;
    font-weight: 700; font-size: 68px; line-height: 1;
    color: var(--ink); letter-spacing: 1px;
  }
  .numbers {
    position: absolute; top: 206px; left: 64px;
    border: 1.5px solid var(--violet); border-radius: 14px;
    padding: 8px 22px;
    font-size: 21px; color: var(--magenta); letter-spacing: 0.5px;
    white-space: nowrap;
  }
  .numbers span.sep { color: var(--violet); margin: 0 10px; }
  .contacts {
    position: absolute; top: 272px; left: 64px;
    list-style: none; font-size: 17px; color: var(--text-grey); font-weight: 400;
  }
  .contacts li { display: flex; align-items: center; gap: 12px; height: 28px; }
  .icon {
    width: 20px; height: 20px; border-radius: 50%;
    background: var(--magenta);
    display: inline-flex; align-items: center; justify-content: center;
  }
  .icon svg { width: 12px; height: 12px; }
  .address {
    position: absolute; top: 276px; right: 64px;
    text-align: right; font-size: 17px; line-height: 1.45; color: var(--text-grey);
    display: flex; gap: 10px; align-items: flex-start;
  }
  .address .icon { background: var(--violet); margin-top: 2px; }
  .services {
    position: absolute; left: 0; right: 0; top: 386px; height: 58px;
    background: var(--band);
    display: flex; align-items: center; justify-content: center;
    color: #fff; font-size: 23px; font-weight: 400; letter-spacing: 1.5px;
    text-transform: uppercase;
  }
  .services .sep { margin: 0 16px; }

  /* ---------- back ---------- */
  .card--back { background: var(--card-dark); }
  .back__brand {
    position: absolute; top: 70px; left: 0; right: 0;
    text-align: center;
    font-weight: 700; font-size: 96px; line-height: 1;
    color: var(--logo-faint);
  }
  .back__service {
    position: absolute; top: 236px; left: 0; right: 0;
    text-align: center;
    font-weight: 600; font-size: 34px; color: #fff;
  }
  .back__band {
    position: absolute; left: 0; right: 0; top: 296px; height: 84px;
    background: var(--band);
    display: flex; align-items: center; justify-content: center;
    font-weight: 700; font-size: 48px; color: #fff; letter-spacing: 1px;
  }
</style>
</head>
<body>
<main class="sheet">

  <section class="card card--front" aria-label="Business card front">
    <div class="brand">
      <span class="brand__dot"></span>
      <span class="brand__name">Bramble Cabs</span>
    </div>

    <p class="front__call">Call: 01832 419 526</p>

    <p class="numbers">
      01832 55 14 14<span class="sep">|</span>01832 30 30 30<span class="sep">|</span>01832 55 72 90
    </p>

    <ul class="contacts">
      <li>
        <span class="icon"><svg viewBox="0 0 24 24" fill="#fff"><path d="M6.6 10.8a15 15 0 0 0 6.6 6.6l2.2-2.2a1 1 0 0 1 1-.25 11.4 11.4 0 0 0 3.6.6 1 1 0 0 1 1 1V20a1 1 0 0 1-1 1A17 17 0 0 1 3 4a1 1 0 0 1 1-1h3.5a1 1 0 0 1 1 1c0 1.25.2 2.45.6 3.6a1 1 0 0 1-.25 1z"/></svg></span>
        0800 555 0 318
      </li>
      <li>
        <span class="icon"><svg viewBox="0 0 24 24" fill="#fff"><path d="M3 6h18v12H3z" fill="none" stroke="#fff" stroke-width="2"/><path d="M3 6l9 7 9-7" fill="none" stroke="#fff" stroke-width="2"/></svg></span>
        bramblecabs@mailbox.co.uk
      </li>
      <li>
        <span class="icon"><svg viewBox="0 0 24 24" fill="none" stroke="#fff" stroke-width="2"><circle cx="12" cy="12" r="9"/><path d="M3 12h18M12 3c3 3 3 15 0 18M12 3c-3 3-3 15 0 18"/></svg></span>
        www.bramblecabs.co.uk
      </li>
    </ul>

    <address class="address" style="font-style: normal;">
      <span>Orchard Lane Hall<br>Mill Yard Oundle<br>PE8 4QX</span>
      <span class="icon"><svg viewBox="0 0 24 24" fill="#fff"><path d="M12 2a7 7 0 0 0-7 7c0 5 7 13 7 13s7-8 7-13a7 7 0 0 0-7-7zm0 9.5A2.5 2.5 0 1 1 12 6.5a2.5 2.5 0 0 1 0 5z"/></svg></span>
    </address>

    <p class="services">
      Airport Transfers<span class="sep">|</span>Minibuses<span class="sep">|</span>School Transport
    </p>
  </section>

  <section class="card card--back" aria-label="Business card back">
    <p class="back__brand">Bramble Cabs</p>
    <p class="back__service">24/7 Service</p>
    <p class="back__band">Call: 01832 419 526</p>
  </section>

</main>
</body>
</html>
```